Bright, Fun and hard to forget home inspection business card.

We need a Business card design for a new Home Inspection company. We are building a brand that is bright, fun and easy to remember.

Target Market(s)

Anyone involed in buying and selling of homes.

Industry/Entity Type

Home Inspection

Contact Information for Business Card

Colin Marlowe Owner/Inspector

Wedsite- PorchAndRafterCheck.example
Phone: 253-555-0187
Email- ColinMarlowe@mailbox.example
WA Lic # 4806

Requirements
Must have
• BRQV LOGO somewhere on card.

```html
<!DOCTYPE html>
<html lang="en">
<head>
<meta charset="utf-8">
<title>Porch &amp; Rafter Check — Business Card</title>
<link rel="stylesheet" href="https://fonts.googleapis.com/css2?family=PT+Sans:wght@400;700&display=swap">
<style>
  :root {
    --orange: #f0623a;
    --charcoal: #1f1e1f;
    --seam: #5a5858;
    --white: #ffffff;
    --grey-text: #a9a6a6;
    --tag-grey: #8c8a8a;
    --backdrop: #efefef;
  }
  * { margin: 0; padding: 0; box-sizing: border-box; }
  html, body { width: 1200px; height: 800px; overflow: hidden; }
  body {
    background: var(--backdrop);
    font-family: "PT Sans", Arial, sans-serif;
    position: relative;
  }
  .card {
    position: absolute;
    top: 252px;
    width: 520px;
    height: 296px;
    background: var(--orange);
    overflow: hidden;
    box-shadow: 0 6px 18px rgba(0,0,0,0.12);
  }
  .card--back { left: 50px; }
  .card--front { left: 630px; }

  .brand-name {
    position: absolute;
    color: var(--white);
    font-weight: 700;
    text-transform: uppercase;
    line-height: 1.05;
    display: flex;
    align-items: center;
    gap: 12px;
  }
  .brand-name__dot {
    width: 16px; height: 16px;
    border-radius: 50%;
    background: var(--white);
    flex: none;
  }
  .card--front .brand-name {
    left: 50%; top: 50%;
    transform: translate(-50%, -50%);
    font-size: 34px;
  }
  .card--back .brand-name {
    left: 40px; top: 78px;
    font-size: 20px;
  }

  .card__curve { position: absolute; inset: 0; }

  .partner-badge {
    position: absolute;
    left: 10px; bottom: 12px;
    width: 22px; height: 22px;
    background: var(--white);
  }

  .contact {
    position: absolute;
    right: 30px;
    top: 92px;
    text-align: right;
    color: var(--orange);
  }
  .contact__name { font-size: 23px; font-weight: 700; line-height: 1; }
  .contact__role { font-size: 12px; color: var(--grey-text); margin-top: 3px; margin-right: 2px; }
  .contact__list { list-style: none; margin-top: 20px; font-size: 15px; line-height: 1.3; }
  .contact__list li { display: flex; justify-content: flex-end; align-items: center; gap: 3px; }
  .contact__tag {
    display: inline-block;
    width: 10px; height: 10px;
    background: var(--tag-grey);
    color: var(--charcoal);
    font-size: 8px;
    line-height: 10px;
    text-align: center;
    font-weight: 700;
  }
  .contact__list .contact__license { margin-right: 13px; }
</style>
</head>
<body>

  <section class="card card--back" aria-label="Business card, contact side">
    <svg class="card__curve" width="520" height="296" viewBox="0 0 520 296" aria-hidden="true">
      <path d="M330 0 C 270 70, 215 170, 175 296 L520 296 L520 0 Z" fill="var(--charcoal)"/>
      <path d="M330 0 C 270 70, 215 170, 175 296" fill="none" stroke="var(--seam)" stroke-width="4"/>
    </svg>

    <div class="brand-name"><span class="brand-name__dot"></span><span>Porch &amp; Rafter<br>Check LLC</span></div>

    <div class="partner-badge" aria-label="Partner badge"></div>

    <div class="contact">
      <p class="contact__name">Colin Marlowe</p>
      <p class="contact__role">Owner/Inspector</p>
      <ul class="contact__list">
        <li>253-555-0187<span class="contact__tag">P</span></li>
        <li>ColinMarlowe@mailbox.example<span class="contact__tag">E</span></li>
        <li>PorchAndRafterCheck.example<span class="contact__tag">W</span></li>
        <li class="contact__license">WA Lic # 4806</li>
      </ul>
    </div>
  </section>

  <section class="card card--front" aria-label="Business card, brand side">
    <div class="brand-name"><span class="brand-name__dot"></span><span>Porch &amp; Rafter<br>Check LLC</span></div>
  </section>

</body>
</html>
```